CD Cover Design Project (Contemporary Country Album)

I am a country singer/songwriter in need of an album cover design (front/back/inside/CD) for my self-titled Nashville-recorded debut-EP release. My musical style is contemporary country/crossover so I want something that has the look and feel of current male country artist album covers (think Corwin Haskett, Ronnie Fallowfield, Grady Pomfret, etc.).

I have attached several photos and a rough mix of the leading track. The CD template can be downloaded here:

http://www.platterforge.net/templates/ecowallets.asp# (4 Panel Eco-Wallet w/ Spine. Jewel Box Size (W139))

I will let you apply your vision (although I do think a more serious look, rather than the one pic where I am smiling, would be best suited for the cover). As mentioned, the album will be self-titled, as "Wendell Trusk".

I really want the album design to show clearly who I am (may need to crop the pictures that are further away) as this will be going to publishing/record companies, etc. The track order for the back and inside is as follows:

1) Wildfire (Velvet Parlour style, song about meeting someone who is in a relationship) - this is the first track and is kind of the feel that should be reflected on at least the main cover

2) Small Words Said Soft (uptempo song about a girl)

3) Missing Every Exit (crossover, about a long distance relationship)

4) Prairie Winds (Harlan Voss style country song)

5) Shots (uptempo, fun party song)

Back Cover - There will need to be some room under the tracks for album credits (producer, etc.) which I will provide upon selecting a designer

Inside - The inside right cover will relist the album tracks and the smaller left panel will have some additional credits and website information (www.wendelltrusk.net)

I hope I have provided enough direction to get the ball rolling, and look forward to seeing your responses.
Updates

A cool, blue color scheme seems to be the direction I want to go, although not too dark.  It should be contemporary, cross-over (to pop) country feel (not classic, traditional country).

Target Market(s)

Contemporary country music fans

Industry/Entity Type

Singer

Requirements
Must have
• Wendell Trusk clearly written as title on cover.

Track listing on back:

1) Wildfire
2) Small Words Said Soft
3) Missing Every Exit
4) Prairie Winds
5) Shots

Room for Producer/songwriting credits below - details TBD once designer is selected.

Inside Right and Left Panels can be worked on once designer is selected as well.

```html
<!DOCTYPE html>
<html lang="en">
<head>
<meta charset="utf-8">
<title>Wendell Trusk – Eco-Wallet Layout</title>
<link href="https://fonts.googleapis.com/css2?family=Exo+2:wght@400;600;700&family=Open+Sans:wght@400;700;800&display=swap" rel="stylesheet">
<style>
  :root {
    --paper: #ffffff;
    --panel: #7599b4;
    --panel-line: #5f83a0;
    --navy: #2b2a5e;
    --gold: #e0a033;
    --photo-dark: #23272c;
    --photo-mid: #4a5057;
    --crop: #9a9a9a;
    --ink: #111111;
    --white: #ffffff;
  }
  html, body { margin: 0; padding: 0; overflow: hidden; background: var(--paper); }
  .canvas { position: relative; width: 1200px; height: 1000px; overflow: hidden; background: var(--paper); font-family: "Exo 2", sans-serif; }
  .dieline { position: absolute; left: 0; top: 0; }
  .abs { position: absolute; margin: 0; }

  /* inside-left panel track list */
  .inside-tracks { left: 172px; top: 460px; color: var(--navy); font-size: 10px; }
  .inside-tracks ol { margin: 0; padding: 0; }
  .inside-tracks li { list-style: none; height: 30px; line-height: 12px; }
  .inside-tracks .song { font-weight: 600; }
  .inside-tracks .credit { display: block; padding-left: 12px; font-size: 9.5px; line-height: 11px; }
  .inside-tracks .credit b { font-weight: 600; font-size: 8.5px; }
  .total-time { left: 175px; top: 614px; color: var(--navy); font-size: 9.5px; }

  /* back panel */
  .back-title { left: 429px; top: 407px; color: var(--white); font-weight: 700; font-size: 30px; letter-spacing: 0.2px; }
  .back-tracks { left: 458px; top: 537px; margin: 0; padding: 0; color: var(--navy); font-size: 12.5px; }
  .back-tracks li { list-style: none; height: 18.6px; line-height: 16px; }
  .back-tracks .num { font-weight: 700; margin-right: 6px; }
  .back-tracks .song { font-weight: 700; }
  .back-tracks .time { font-weight: 400; margin-left: 4px; }
  .legal { left: 463px; top: 657px; width: 200px; font-family: "Open Sans", sans-serif; font-size: 4.2px; line-height: 5.6px; color: var(--ink); }
  .legal b { font-weight: 800; }
  .credits { left: 672px; top: 650px; width: 90px; font-family: "Open Sans", sans-serif; font-size: 5.4px; line-height: 7.3px; color: var(--ink); }

  /* spine */
  .spine { left: 768px; top: 405px; writing-mode: vertical-rl; color: var(--gold); font-size: 7px; font-weight: 700; letter-spacing: 1.5px; }

  /* front cover */
  .cover-name { left: 845px; top: 605px; color: var(--gold); font-weight: 700; font-size: 37px; letter-spacing: -0.5px; line-height: 1; }

  .status-note { left: 731px; top: 725px; font-family: "Open Sans", sans-serif; font-weight: 800; font-size: 20px; color: var(--ink); letter-spacing: -0.2px; white-space: nowrap; }
</style>
</head>
<body>
<div class="canvas">
  <svg class="dieline" width="1200" height="1000" viewBox="0 0 1200 1000">
    <g stroke="var(--crop)" stroke-width="1">
      <line x1="788" y1="25" x2="788" y2="40"/><line x1="1151" y1="25" x2="1151" y2="40"/>
      <line x1="764" y1="48" x2="779" y2="48"/><line x1="1158" y1="48" x2="1173" y2="48"/>
      <line x1="49" y1="355" x2="49" y2="366"/><line x1="406" y1="355" x2="406" y2="366"/>
      <line x1="774" y1="355" x2="774" y2="366"/>
      <line x1="25" y1="376" x2="40" y2="376"/><line x1="1158" y1="376" x2="1173" y2="376"/>
      <line x1="25" y1="699" x2="40" y2="699"/><line x1="1158" y1="699" x2="1173" y2="699"/>
      <line x1="49" y1="709" x2="49" y2="725"/><line x1="406" y1="709" x2="406" y2="725"/>
      <line x1="774" y1="709" x2="774" y2="725"/><line x1="1151" y1="709" x2="1151" y2="725"/>
    </g>
    <rect class="flap" x="780" y="41" width="377" height="327" fill="var(--panel)"/>
    <path class="inside-left" d="M41,367 H406 V708 H41 V585 Q41,561 70,561 H112 A23.5,23.5 0 0 0 112,514 H70 Q41,514 41,488 Z" fill="var(--panel)"/>
    <rect class="back-panel" x="405" y="366" width="375" height="343" fill="var(--panel)"/>
    <rect x="413" y="380" width="354" height="314" fill="none" stroke="var(--panel-line)" stroke-width="1.5"/>
    <line x1="428" y1="367" x2="428" y2="626" stroke="var(--gold)" stroke-width="1"/>
    <g stroke="var(--gold)" stroke-width="0.8">
      <line x1="428" y1="552" x2="750" y2="552"/>
      <line x1="428" y1="571" x2="750" y2="571"/>
      <line x1="428" y1="589" x2="750" y2="589"/>
      <line x1="428" y1="608" x2="750" y2="608"/>
      <line x1="428" y1="626" x2="750" y2="626"/>
    </g>
    <rect class="front-panel" x="780" y="366" width="378" height="343" fill="var(--panel)"/>
    <defs>
      <radialGradient id="coverPhoto" cx="0.3" cy="0.4" r="0.8">
        <stop offset="0" stop-color="var(--photo-mid)"/>
        <stop offset="1" stop-color="var(--photo-dark)"/>
      </radialGradient>
    </defs>
    <rect x="782" y="369" width="373" height="337" fill="url(#coverPhoto)" role="img" aria-label="Black-and-white portrait of the singer in a plaid shirt holding an electric guitar against a dark blurred street background"/>
    <line x1="782" y1="381" x2="1155" y2="381" stroke="var(--panel-line)" stroke-width="1"/>
    <line x1="782" y1="692" x2="1155" y2="692" stroke="var(--panel-line)" stroke-width="1"/>
  </svg>

  <div class="abs inside-tracks">
    <ol>
      <li><span class="song">1&nbsp; Wildfire</span>&nbsp; 0'00<span class="credit"><b>composer</b> Lionel Farrow, <b>composer</b> Wendell Trusk</span></li>
      <li><span class="song">2&nbsp; Small Words Said Soft</span>&nbsp; 0'00<span class="credit"><b>composer</b> Lionel Farrow, <b>composer</b> Wendell Trusk</span></li>
      <li><span class="song">3&nbsp; Missing Every Exit</span>&nbsp; 0'00<span class="credit"><b>composer</b> Lionel Farrow, <b>composer</b> Wendell Trusk</span></li>
      <li><span class="song">4&nbsp; Prairie Winds</span>&nbsp; 0'00<span class="credit"><b>composer</b> Lionel Farrow, <b>composer</b> Wendell Trusk</span></li>
      <li><span class="song">5&nbsp; Shots</span>&nbsp; 0'00<span class="credit"><b>composer</b> Lionel Farrow, <b>composer</b> Wendell Trusk</span></li>
    </ol>
  </div>
  <p class="abs total-time">Total time: 00'00</p>

  <h1 class="abs back-title">Wendell Trusk</h1>
  <ol class="abs back-tracks">
    <li><span class="num">1</span><span class="song">Wildfire</span><span class="time">0'00</span></li>
    <li><span class="num">2</span><span class="song">Small Words Said Soft</span><span class="time">0'00</span></li>
    <li><span class="num">3</span><span class="song">Missing Every Exit</span><span class="time">0'00</span></li>
    <li><span class="num">4</span><span class="song">Prairie Winds</span><span class="time">0'00</span></li>
    <li><span class="num">5</span><span class="song">Shots</span><span class="time">0'00</span></li>
  </ol>
  <p class="abs legal"><b>http://www.halcyonaudio.com</b> © 2013 Halcyon Audio Group Inc. Manufactured by Halcyon Audio Group Inc. / 118 Harbor Lane, Fairmont, NY 10400. WARNING: All rights reserved, including all rights of the producer and of the owners of the recorded work. Unauthorized copying, public performance, broadcasting, hiring or rental of this recording prohibited, as provided by applicable law. <b>Distribution: Halcyon Audio.</b></p>
  <p class="abs credits">Composer: Wendell Trusk<br>Producers: Lionel Farrow &amp; Wendell Trusk<br>Engineer: Pete Marlow<br>Photography: Curtis Bellamy<br>Design: Tessa Quill</p>

  <p class="abs spine">WENDELL TRUSK</p>

  <p class="abs cover-name">Wendell Trusk</p>

  <p class="abs status-note">Unfinished concept - final to be posted shortly</p>
</div>
</body>
</html>
```